Business Card

I need a business card that is fresh, styling and reflects my heart centered healing business while still maintaining full professionalism as I have an my evidence-based practice. I am a Naturopath and a Shiatsu Massage Therapist.
Below are my existing logo (file 1) and an inspiration image (file 2) that reflects the colours and style I would like to express to my card (blues greens). I especially like that tree wallpaper.

Information for the card:
Tessa Gorrinde
BHSc. (Nat) m.QRPC
Naturopath
Herbalist
Nutritionist
Shiatsu Therapist
Wellness Counsellor

41 Dovertan St South Fremantle
www.tessagorrinde.com.au
tessa@tessagorrinde.com.au

NOte: I've removed part of the brief, in that I've changed my mind about the back of the card being a '5 treatments and get sixth one free" I'd rather have this on a separate card. So please do not include this in your designs.
Updates

Hi Guys, I've taken the '5 session get the sixth free' part out of the brief. Also, I've added the info to go on the business card into the brief.

Thanks and happy designing
Tes

I've just uploaded a high res better quality version of the hand logo. Thanks Lovlies. 

Target Market(s)

I am targeting western women of ages 25 - 40 in preconception care, sugar addiction therapy, and wellness coaching. I want must card to be vibrant, positive and current.

Industry/Entity Type

Business

Requirements
Must have
• Please include my hand image logo

```html
<!DOCTYPE html>
<html lang="en">
<head>
<meta charset="utf-8">
<title>Tessa Gorrinde – Business Card</title>
<link href="https://fonts.googleapis.com/css2?family=Questrial&family=Arimo:wght@400&display=swap" rel="stylesheet">
<style>
  :root {
    --page: #ffffff;
    --mint: #8ddfb0;
    --teal-light: #88cfc8;
    --blue-light: #86bccf;
    --lime-light: #e8f58a;
    --ring-green: #1dc05a;
    --ring-teal: #0b9186;
    --ring-blue: #0d6d9a;
    --ring-lime: #d8ec10;
    --ink: #1d5a58;
    --ink-dark: #1e4a4c;
    --label: #ffffff;
    --label-shade: #3d4a4a;
  }
  * { margin: 0; padding: 0; box-sizing: border-box; }
  html, body {
    width: 1200px;
    height: 686px;
    overflow: hidden;
    background: var(--page);
  }
  .card {
    position: absolute;
    left: 31px;
    top: 31px;
    width: 1140px;
    height: 591px;
    font-family: "Questrial", sans-serif;
  }
  .quadrant { position: absolute; }
  .quadrant--tl { left: 0; top: 0; width: 560px; height: 295px; background: var(--mint); }
  .quadrant--tr { left: 560px; top: 0; width: 580px; height: 295px; background: var(--teal-light); }
  .quadrant--bl { left: 0; top: 295px; width: 560px; height: 296px; background: var(--blue-light); }
  .quadrant--br { left: 560px; top: 295px; width: 580px; height: 296px; background: var(--lime-light); }
  .ring {
    position: absolute;
    left: 0; top: 0;
    width: 1140px; height: 591px;
  }
  .name {
    position: absolute;
    left: 24px; top: 8px;
    font-size: 58px;
    font-weight: 400;
    color: var(--ink);
    letter-spacing: 0.5px;
  }
  .credentials {
    position: absolute;
    left: 26px; top: 79px;
    font-size: 28px;
    color: var(--ink);
  }
  .address {
    position: absolute;
    left: 578px; top: 24px;
    font-size: 29px;
    color: var(--ink-dark);
  }
  .website {
    position: absolute;
    left: 38px; top: 549px;
    font-size: 31px;
    color: var(--ink-dark);
  }
  .email {
    position: absolute;
    left: 580px; top: 549px;
    font-size: 31px;
    color: var(--ink-dark);
  }
  .service {
    position: absolute;
    font-family: "Arimo", sans-serif;
    font-size: 33px;
    line-height: 47px;
    color: var(--label);
    letter-spacing: -0.5px;
    text-shadow: 0 0 2px var(--label-shade), 1px 1px 2px var(--label-shade), -1px -1px 1px var(--label-shade);
  }
  .service--left { text-align: right; }
  .service--naturopath { right: 650px; top: 210px; }
  .service--herbal { left: 642px; top: 180px; }
  .service--shiatsu { right: 656px; top: 326px; }
  .service--wellness { left: 642px; top: 331px; }
  .centre-name {
    position: absolute;
    left: 460px; top: 280px;
    width: 200px;
    text-align: center;
    font-size: 21px;
    line-height: 26px;
    color: var(--ink-dark);
  }
</style>
</head>
<body>
  <main class="card">
    <div class="quadrant quadrant--tl"></div>
    <div class="quadrant quadrant--tr"></div>
    <div class="quadrant quadrant--bl"></div>
    <div class="quadrant quadrant--br"></div>

    <svg class="ring" viewBox="0 0 1140 591" aria-hidden="true">
      <g fill="none" stroke-width="80">
        <path d="M 417 295 A 143 143 0 0 1 560 152" stroke="var(--ring-green)"/>
        <path d="M 560 152 A 143 143 0 0 1 703 295" stroke="var(--ring-teal)"/>
        <path d="M 703 295 A 143 143 0 0 1 560 438" stroke="var(--ring-lime)"/>
        <path d="M 560 438 A 143 143 0 0 1 417 295" stroke="var(--ring-blue)"/>
      </g>
      <circle cx="560" cy="295" r="100" fill="#ffffff" fill-opacity="0.4"/>
      <g stroke="#ffffff" stroke-width="3">
        <line x1="560" y1="0" x2="560" y2="591"/>
        <line x1="0" y1="295" x2="1140" y2="295"/>
      </g>
    </svg>

    <h1 class="name">Tessa Gorrinde</h1>
    <p class="credentials">BHSc. (Nat) m.QRPC</p>
    <p class="address">41 Dovertan St South Fremantle</p>

    <p class="centre-name">Tessa<br>Gorrinde</p>

    <p class="service service--left service--naturopath">Naturopath</p>
    <p class="service service--herbal">Herbalist<br>Nutritionist</p>
    <p class="service service--left service--shiatsu">Shiatsu<br>Therapist</p>
    <p class="service service--wellness">Wellness<br>Counsellor</p>

    <p class="website">www.tessagorrinde.com.au</p>
    <p class="email">tessa@tessagorrinde.com.au</p>
  </main>
</body>
</html>
```